Business Card Design Project - Small Bar

We would like a design for a business card for our new small bar in Melbourne. It is quite the 'hipster' bar and the card would need to reflect this in its design. We do have a logo which needs to be used in the card, tho how it is incorporated is up to you! :)

OK, the Bar currently has a common 'inner city' vibe, i.e. random artwork, older 30s/40's club furniture, grafitti murals on the walls, eclectic objects etc etc Current clientele would be described as "hipster", "urban professional" etc. How to describe... they are 30, have a good job but have beards, beanies and own vinyl records. :)

The card will be used to give to professional contacts and to bands/solo artists we come across to invite them to come play at our venue, so somehow I would like it to convey the image of 'professional' and 'funky' all in one. Difficult I know.

I have asked for some advice on making this brief clearer, so check back.

Thanks all in advance. :)
Updates

Sorry all

I've now been told that it is WEST MELBOURNE 3003. Apparently we are on the border and it is referred to by either west or north Melbourne, but it is definitely West Melbourne 3003.

Things you learn hey? :)

Target Market(s)

Hipsters, urbanites, the inner city crowd

Industry/Entity Type

Artists

Requirements
Must have
Name of the bar "The Lantern & Badger"
Address - 128 Pembury St, Pembury Vale, Victoria 3990
Names - Paul Redfern, Dean Horwick
mobile. 0417265930 and 0439572614
Obviously we would need separate cards?
Nice to have
• Facebook link
Facebook 'like' icon
Should not have
• traditional designs. I am looking for something unique and funky. with FUNK! :)

```html
<!DOCTYPE html>
<html lang="en">
<head>
<meta charset="utf-8">
<title>The Lantern &amp; Badger – Business Card</title>
<link rel="stylesheet" href="https://fonts.googleapis.com/css2?family=Gabriela&display=swap">
<style>
  :root {
    --backdrop: #969696;
    --card: #ffffff;
    --ink: #1a1a1a;
  }
  html, body {
    margin: 0;
    padding: 0;
    width: 1200px;
    height: 1000px;
    overflow: hidden;
    background: var(--backdrop);
  }
  .canvas {
    position: relative;
    width: 1200px;
    height: 1000px;
  }
  .card {
    position: absolute;
    left: 340px;
    top: 30px;
    width: 522px;
    height: 938px;
    background: var(--card);
    color: var(--ink);
    font-family: "Gabriela", serif;
    text-align: center;
  }
  .brand-mark {
    position: absolute;
    left: 86px;
    top: 125px;
    width: 350px;
    height: 350px;
  }
  .brand-name {
    position: absolute;
    left: 86px;
    top: 262px;
    width: 350px;
    font-size: 30px;
    line-height: 1.15;
    letter-spacing: 2px;
    text-transform: uppercase;
    margin: 0;
    font-weight: 400;
  }
  .brand-address {
    position: absolute;
    left: 86px;
    top: 490px;
    width: 350px;
    font-size: 14px;
    letter-spacing: 1.5px;
    text-transform: uppercase;
    line-height: 1.4;
    margin: 0;
  }
  .contact {
    position: absolute;
    left: 0;
    top: 664px;
    width: 522px;
  }
  .contact p {
    transform: scaleX(0.78);
    transform-origin: center;
  }
  .contact-name {
    font-size: 34px;
    text-transform: uppercase;
    margin: 0;
    line-height: 1;
  }
  .contact-role {
    font-size: 17px;
    text-transform: uppercase;
    margin: 6px 0 0;
    line-height: 1;
  }
  .contact-phone {
    font-size: 40px;
    margin: 16px 0 0;
    line-height: 1;
  }
  .web-link {
    position: absolute;
    left: 0;
    bottom: 18px;
    width: 522px;
    font-size: 15px;
    text-transform: uppercase;
    letter-spacing: 0.4px;
    margin: 0;
  }
</style>
</head>
<body>
<main class="canvas">
  <section class="card">
    <svg class="brand-mark" viewBox="0 0 350 350" aria-hidden="true">
      <circle cx="175" cy="175" r="170" fill="none" stroke="var(--ink)" stroke-width="2"/>
    </svg>
    <h1 class="brand-name">The Lantern<br>&amp; Badger</h1>
    <p class="brand-address">128 Pembury St, Pembury Vale<br>Victoria 3990</p>

    <div class="contact">
      <p class="contact-name">Paul Redfern</p>
      <p class="contact-role">(Director)</p>
      <p class="contact-phone">0417265930</p>
    </div>

    <p class="web-link">www.badgerbook.net/pages/the-lantern-and-badger</p>
  </section>
</main>
</body>
</html>
```